tile distributor needs a new logo and packaging designe

"BREVALO TILE & STONE LTD'' in Canada needs great logo and a graphic design for a cardboard box package for the ceramic tiles. For inspiration you can use the logo from our sister's company, www.brevalo-example.de.
In regards to the cardboard package for the ceramic tiles it should include the BREVALO new logo on white cardboard background.
The box has to have the following info:
-Company name (with slogan "ARCHITECTURAL SOLUTIONS" or similar)
-Nominal size of the tiles (we need packages for 30cm x 60cm, 60cm x 60cm,and 30cm x 90cm) with table: nominal thickness, #pieces per box and MQ/SFT per box
-product description "RECTIFIED PORCELAIN TILE"
-made in china (not too visible, small letters)
-CE sign
-Attention text:"Before tile setting, please verify...." (see the attachment)
-Emission in indoor air sign
-and the hole on the front page (the color of the tile should be visible)
All text will be translated in 3 languages (German, English and Serbian)
I have attached some samples of the competitor"s packages and our current box for your reference.
I have increased the budget for CND$100 for my project and I hope that now it will be more atractiv for designers.
Looking forward to seeing your fresh ideas.
Reason: I have just increased the budget for this project therefore I am extending the deadline.
Hope this will help to get the great design for my company logo and packaging.

```html
<!DOCTYPE html>
<html lang="en">
<head>
<meta charset="utf-8">
<title>Brevalo Tile &amp; Stone – Tile Box Dieline</title>
<link rel="stylesheet" href="https://fonts.googleapis.com/css2?family=Archivo:wght@400;500;700;800;900&display=swap">
<style>
  :root {
    --ink: #000000;
    --paper: #ffffff;
    --pattern-tone: #7a7a7a;
  }
  html, body {
    margin: 0;
    padding: 0;
    width: 1200px;
    height: 1000px;
    overflow: hidden;
    background: var(--paper);
  }
  .dieline {
    display: block;
    width: 1200px;
    height: 1000px;
    font-family: "Archivo", Arial, sans-serif;
  }
  .cut { fill: var(--paper); stroke: var(--ink); stroke-width: 1; }
  .band { fill: var(--ink); }
  .gap { fill: var(--paper); }
  .rail { fill: none; stroke: var(--ink); stroke-width: 6; stroke-linejoin: miter; }
  .pattern { fill: var(--pattern-tone); }
  .pattern-framed { fill: var(--ink); }
  .mark-square { fill: var(--ink); }
  .mark-square.on-dark { fill: var(--paper); }
  .brand-name { font-weight: 800; fill: var(--ink); }
  .brand-sub { font-weight: 400; fill: var(--ink); letter-spacing: 1.5px; }
  .on-dark { fill: var(--paper); }
  .rule { stroke: var(--ink); stroke-width: 1.5; }
  .rule.on-dark { stroke: var(--paper); }
  .product-title { font-weight: 900; font-size: 29px; fill: var(--ink); letter-spacing: 0.5px; }
  .origin { font-size: 8px; fill: var(--ink); }
  .count { font-weight: 900; fill: var(--ink); }
  .size-label { font-weight: 900; font-size: 42px; fill: var(--ink); letter-spacing: 1px; }
  .window { fill: var(--paper); stroke: var(--ink); stroke-width: 1.2; }
  .lang-tag { fill: var(--ink); }
  .lang-code { font-weight: 800; font-size: 8px; fill: var(--paper); }
  .notice { font-size: 8.6px; font-weight: 500; fill: var(--ink); }
  .notice-divider { stroke: var(--ink); stroke-width: 2; }
  .spec-table line { stroke: var(--paper); stroke-width: 1.5; }
  .spec-table rect { fill: none; stroke: var(--paper); stroke-width: 1.5; }
  .ce-mark { font-size: 20px; font-weight: 400; fill: var(--paper); }
  .ce-note { font-size: 9px; font-weight: 500; fill: var(--paper); }
</style>
</head>
<body>
<svg class="dieline" viewBox="0 0 1200 1000" xmlns="http://www.w3.org/2000/svg">

  <!-- Flaps -->
  <g class="flaps">
    <polygon class="cut" points="275,101 290,31 910,31 925,101"/>
    <polygon class="cut" points="275,897 290,967 910,967 925,897"/>
    <polygon class="cut" points="203,172 131,186 131,812 203,826"/>
    <polygon class="cut" points="998,172 1069,186 1069,812 998,826"/>
    <polygon class="cut" points="203,172 208,108 263,108 275,172"/>
    <polygon class="cut" points="925,172 935,108 990,108 998,172"/>
    <polygon class="cut" points="203,826 208,834 208,890 263,890 275,826"/>
    <polygon class="cut" points="925,826 935,890 990,890 998,834 998,826"/>
  </g>

  <!-- Bands -->
  <g class="bands">
    <rect class="band" x="275" y="101" width="650" height="71"/>
    <rect class="band" x="275" y="826" width="650" height="71"/>
    <rect class="band" x="203" y="172" width="72" height="654"/>
    <rect class="band" x="926" y="172" width="72" height="654"/>
    <rect class="gap" x="348" y="101" width="89" height="71"/>
    <rect class="gap" x="348" y="826" width="89" height="71"/>
  </g>

  <!-- Running rails -->
  <g class="rails">
    <polyline class="rail" points="348,22 348,270 473,270 473,384 348,384 348,975"/>
    <polyline class="rail" points="437,22 437,313 313,313 313,432 437,432 437,975"/>
  </g>

  <!-- Key pattern areas -->
  <rect class="pattern-framed" x="355" y="446" width="77" height="366" role="img" aria-label="Vertical key-pattern ornament strip in a black frame"/>
  <rect class="pattern" x="218" y="432" width="48" height="356" role="img" aria-label="White key-pattern ornament on the black side band"/>
  <rect class="pattern" x="935" y="208" width="50" height="354" role="img" aria-label="White key-pattern ornament on the black side band"/>

  <!-- Top band (upside down) -->
  <g class="brand-lockup top" transform="rotate(180 600 136)">
    <rect class="mark-square on-dark" x="560" y="110" width="45" height="45"/>
    <text class="brand-name on-dark" x="617" y="144" font-size="26">BREVALO</text>
    <line class="rule on-dark" x1="617" y1="151" x2="737" y2="151"/>
    <text class="brand-sub on-dark" x="617" y="164" font-size="11">TILE &amp; STONE LTD</text>
  </g>
  <g class="spec-table">
    <rect x="660" y="121" width="238" height="36"/>
    <line x1="660" y1="133" x2="898" y2="133"/>
    <line x1="660" y1="145" x2="898" y2="145"/>
    <line x1="706" y1="121" x2="706" y2="157"/>
    <line x1="750" y1="121" x2="750" y2="157"/>
    <line x1="795" y1="121" x2="795" y2="157"/>
  </g>

  <!-- Front panel lockup -->
  <g class="brand-lockup front">
    <rect class="mark-square" x="594" y="204" width="78" height="78"/>
    <text class="brand-name" x="878" y="240" font-size="36" text-anchor="end">BREVALO</text>
    <line class="rule" x1="692" y1="253" x2="878" y2="253"/>
    <text class="brand-sub" x="878" y="282" font-size="16" text-anchor="end">TILE &amp; STONE LTD</text>
  </g>

  <g class="product-info">
    <text class="product-title" x="878" y="338" text-anchor="end">RECTIFIED</text>
    <text class="product-title" x="878" y="372" text-anchor="end">PORCELAIN</text>
    <text class="product-title" x="878" y="406" text-anchor="end">TILE</text>
    <text class="origin" x="878" y="429" text-anchor="end">MADE IN CHINA</text>
    <text class="count" x="878" y="488" font-size="46" text-anchor="end">10</text>
    <text class="count" x="878" y="516" font-size="21" text-anchor="end" letter-spacing="2">PCS</text>
  </g>

  <rect class="window" x="614" y="538" width="260" height="256"/>

  <text class="size-label" transform="translate(327 630) rotate(-90)" text-anchor="middle">600 x 600 mm</text>

  <!-- Notice text in three languages -->
  <g class="notice-block">
    <rect class="lang-tag" x="463" y="533" width="18" height="10"/>
    <text class="lang-code" x="466" y="541">GB</text>
    <text class="notice" x="485" y="541">Lorem ipsum dolor sit</text>
    <text class="notice" x="463" y="551">amet, consectetur adipiscing</text>
    <text class="notice" x="463" y="561">elit. Cras in lorem ut ante luctus</text>
    <text class="notice" x="463" y="571">laoreet sit amet vel turpis.</text>
    <text class="notice" x="463" y="581">Quisque ornare gravida nisl quis</text>
    <text class="notice" x="463" y="591">tristique. Nulla ullamcorper</text>
    <text class="notice" x="463" y="601">metus sit amet quam rhoncus,</text>
    <text class="notice" x="463" y="611">eu blandit ligula malesuada.</text>
    <line class="notice-divider" x1="460" y1="618" x2="611" y2="618"/>

    <rect class="lang-tag" x="463" y="623" width="18" height="10"/>
    <text class="lang-code" x="466" y="631">ES</text>
    <text class="notice" x="485" y="631">Lorem ipsum dolor sit</text>
    <text class="notice" x="463" y="641">amet, consectetur adipiscing</text>
    <text class="notice" x="463" y="651">elit. Cras in lorem ut ante luctus</text>
    <text class="notice" x="463" y="661">laoreet sit amet vel turpis.</text>
    <text class="notice" x="463" y="671">Quisque ornare gravida nisl quis</text>
    <text class="notice" x="463" y="681">tristique. Nulla ullamcorper</text>
    <text class="notice" x="463" y="691">metus sit amet quam rhoncus,</text>
    <text class="notice" x="463" y="701">eu blandit ligula malesuada.</text>
    <line class="notice-divider" x1="460" y1="708" x2="611" y2="708"/>

    <rect class="lang-tag" x="463" y="713" width="16" height="10"/>
    <text class="lang-code" x="468" y="721">F</text>
    <text class="notice" x="485" y="721">Lorem ipsum dolor sit</text>
    <text class="notice" x="463" y="731">amet, consectetur adipiscing</text>
    <text class="notice" x="463" y="741">elit. Cras in lorem ut ante luctus</text>
    <text class="notice" x="463" y="751">laoreet sit amet vel turpis.</text>
    <text class="notice" x="463" y="761">Quisque ornare gravida nisl quis</text>
    <text class="notice" x="463" y="771">tristique. Nulla ullamcorper</text>
    <text class="notice" x="463" y="781">metus sit amet quam rhoncus,</text>
    <text class="notice" x="463" y="791">eu blandit ligula malesuada.</text>
  </g>

  <!-- Left band lockup (reads top to bottom) -->
  <g class="brand-lockup left">
    <rect class="mark-square on-dark" x="218" y="208" width="46" height="46"/>
    <g transform="translate(246 268) rotate(90)">
      <text class="brand-name on-dark" x="0" y="0" font-size="22">BREVALO</text>
    </g>
    <line class="rule on-dark" x1="233" y1="268" x2="233" y2="380"/>
    <g transform="translate(217 268) rotate(90)">
      <text class="brand-sub on-dark" x="0" y="0" font-size="10.5">TILE &amp; STONE LTD</text>
    </g>
  </g>

  <!-- Right band lockup (reads bottom to top) -->
  <g class="brand-lockup right">
    <rect class="mark-square on-dark" x="936" y="738" width="48" height="48"/>
    <g transform="translate(956 726) rotate(-90)">
      <text class="brand-name on-dark" x="0" y="0" font-size="22">BREVALO</text>
    </g>
    <line class="rule on-dark" x1="966" y1="614" x2="966" y2="726"/>
    <g transform="translate(986 726) rotate(-90)">
      <text class="brand-sub on-dark" x="0" y="0" font-size="10.5">TILE &amp; STONE LTD</text>
    </g>
  </g>

  <!-- Bottom band -->
  <g class="brand-lockup bottom">
    <rect class="mark-square on-dark" x="470" y="838" width="48" height="48"/>
    <text class="brand-name on-dark" x="528" y="864" font-size="24">BREVALO</text>
    <line class="rule on-dark" x1="528" y1="871" x2="640" y2="871"/>
    <text class="brand-sub on-dark" x="528" y="888" font-size="11">TILE &amp; STONE LTD</text>
  </g>

  <g class="compliance">
    <text class="ce-mark" transform="translate(806 873) rotate(-90)" text-anchor="middle">CE</text>
    <g transform="translate(826 893) rotate(-90)">
      <text class="ce-note" x="0" y="0">Cras purus</text>
      <text class="ce-note" x="0" y="11">felis,</text>
      <text class="ce-note" x="0" y="22">imperdiet</text>
      <text class="ce-note" x="0" y="33">vitae lacinia</text>
      <text class="ce-note" x="0" y="44">aliquet,</text>
      <text class="ce-note" x="0" y="55">tristique</text>
      <text class="ce-note" x="0" y="66">vulputate</text>
      <text class="ce-note" x="0" y="77">eros</text>
    </g>
  </g>

</svg>
</body>
</html>
```